Business Card Design Project

Financial planning, Insurance and Real estate - Financial Services company

Contact Information for Business Card

Looking for something simple in design -
Tolverin Equity LLC
Tolverin Wealth Managment

```html
<!DOCTYPE html>
<html lang="en">
<head>
<meta charset="utf-8">
<title>Tolverin Wealth Management – Business Card</title>
<link rel="stylesheet" href="https://fonts.googleapis.com/css2?family=Open+Sans:wght@400;700&display=swap">
<style>
  :root {
    --brand-blue: #0682c4;
    --card-white: #fbfbfa;
    --page-bg: #e9ebee;
    --ink-white: #ffffff;
  }
  * { margin: 0; padding: 0; box-sizing: border-box; }
  html, body {
    width: 1200px;
    height: 900px;
    overflow: hidden;
    background: var(--page-bg);
    font-family: "Open Sans", Arial, sans-serif;
  }
  .business-card {
    position: absolute;
    left: 150px;
    top: 171px;
    width: 900px;
    height: 558px;
    background: var(--card-white);
    overflow: hidden;
    box-shadow: 0 10px 30px rgba(0, 0, 0, 0.15);
  }
  .card-shapes {
    position: absolute;
    inset: 0;
  }
  .company-name {
    position: absolute;
    left: 212px;
    top: 296px;
    transform: translateX(-50%);
    white-space: nowrap;
    font-size: 22px;
    font-weight: 700;
    color: var(--brand-blue);
    letter-spacing: -0.2px;
  }
  .contact-block {
    position: absolute;
    right: 44px;
    top: 156px;
    text-align: right;
    color: var(--ink-white);
  }
  .person-name {
    font-size: 27px;
    font-weight: 400;
    line-height: 34px;
    letter-spacing: 0.3px;
  }
  .person-title {
    font-size: 23px;
    line-height: 30px;
  }
  .contact-list, .service-list {
    list-style: none;
    font-size: 22px;
    line-height: 33px;
  }
  .contact-list { margin-top: 28px; }
  .service-list { margin-top: 27px; line-height: 34px; }
  .contact-list li, .service-list li {
    display: flex;
    justify-content: flex-end;
    align-items: center;
    gap: 6px;
  }
  .contact-icon { width: 18px; height: 18px; flex: none; }
  .service-dot {
    width: 12px;
    height: 12px;
    border-radius: 50%;
    background: var(--ink-white);
    flex: none;
    margin-left: 3px;
  }
</style>
</head>
<body>
  <div class="business-card">
    <svg class="card-shapes" width="900" height="558" viewBox="0 0 900 558">
      <path class="blue-panel" fill="var(--brand-blue)"
            d="M748 0 H900 V558 H341 C420 330 560 150 748 0 Z"/>
      <path class="accent-swoosh" fill="var(--brand-blue)"
            d="M728 0 H738 C545 150 402 330 328 558 H317 C385 330 530 150 728 0 Z"/>
    </svg>

    <div class="company-name">Tolverin Wealth Management</div>

    <div class="contact-block">
      <div class="person-name">MARCUS HALE</div>
      <div class="person-title">Managing Director</div>

      <ul class="contact-list">
        <li>044-310 582 647
          <svg class="contact-icon" viewBox="0 0 18 18" aria-label="mobile">
            <rect x="5" y="1" width="8" height="16" rx="1.5" fill="none" stroke="#fff" stroke-width="1.6"/>
            <rect x="7.5" y="13.5" width="3" height="1.5" fill="#fff"/>
          </svg>
        </li>
        <li>044-310 582 647
          <svg class="contact-icon" viewBox="0 0 18 18" aria-label="telephone">
            <path d="M2 7 C2 3 16 3 16 7 L13 8 L12 6 H6 L5 8 Z" fill="#fff"/>
            <path d="M4 9 H14 L15 16 H3 Z" fill="#fff"/>
          </svg>
        </li>
        <li>info@tolverinwm.com
          <svg class="contact-icon" viewBox="0 0 18 18" aria-label="email">
            <rect x="1.5" y="4" width="15" height="10" fill="#fff"/>
            <path d="M1.5 4 L9 10 L16.5 4" fill="none" stroke="var(--brand-blue)" stroke-width="1.3"/>
          </svg>
        </li>
        <li>www.tolverinwm.com
          <svg class="contact-icon" viewBox="0 0 18 18" aria-label="website">
            <circle cx="9" cy="9" r="7.5" fill="#fff"/>
            <path d="M5 6 C7 5 8 7 7 9 C6 11 8 12 8 14 M11 4 C12 6 14 6 14 8 C12 9 11 11 12 13" fill="none" stroke="var(--brand-blue)" stroke-width="1.2"/>
          </svg>
        </li>
      </ul>

      <ul class="service-list">
        <li>Financial Planning <span class="service-dot"></span></li>
        <li>Insurance <span class="service-dot"></span></li>
        <li>Real Estate <span class="service-dot"></span></li>
      </ul>
    </div>
  </div>
</body>
</html>
```